Letterhead for Law Firm - Logo already prepared

I previously used to prepare a logo which I was quite pleased with, a copy is attached for your reference. I would like the font of the logo to be all the same size, rather than the 'S' and 'L' being larger than the other letters.
I have copies of the attached in other formats if necessary.
I need a letterhead prepared which is virtually identical to the draft attached, however I will be adding an address, phone number, fax number, mobile number and email. I will provide these details with whoever can assist me.
I will also be providing insurance details to be listed at the foot of the page.
Finally, I need the file to be supplied as a high resolution pdf with 2mm bleed.
If you require any further information, please do not hesitate to contact me.

```html
<!DOCTYPE html>
<html lang="en">
<head>
<meta charset="utf-8">
<title>Hartwell Legal — Letterhead</title>
<link href="https://fonts.googleapis.com/css2?family=Montserrat:wght@400;500;600&display=swap" rel="stylesheet">
<style>
  :root {
    --backdrop: #2b2b2d;
    --paper: #ffffff;
    --paper-shade: #eeeeee;
    --ink: #2e2e2e;
    --ink-soft: #555555;
    --contact-red: #b8382a;
    --brand-orange: #e8870e;
    --amber: #f2a516;
    --rust: #a3401a;
  }
  * { box-sizing: border-box; margin: 0; padding: 0; }
  html, body {
    width: 1200px; height: 900px; overflow: hidden;
    background: var(--backdrop);
    font-family: "Montserrat", sans-serif;
  }
  .canvas {
    position: relative; width: 1200px; height: 900px;
    display: flex; align-items: center; justify-content: center;
  }
  .letterhead {
    position: relative; width: 608px; height: 860px;
    background: radial-gradient(ellipse at 50% 40%, var(--paper) 55%, var(--paper-shade) 100%);
    overflow: hidden;
    box-shadow: 0 10px 40px rgba(0,0,0,.5);
  }
  .letterhead__header {
    position: absolute; top: 38px; left: 38px; right: 34px;
    display: flex; justify-content: space-between; align-items: flex-start;
  }
  .brand { display: flex; align-items: center; gap: 9px; }
  .brand__dot {
    width: 26px; height: 26px; border-radius: 50%;
    background: var(--brand-orange);
  }
  .brand__name {
    font-weight: 500; font-size: 15px; letter-spacing: .04em;
    color: var(--ink); text-transform: uppercase;
  }
  .contact {
    display: flex; gap: 7px; font-style: normal;
    font-size: 5.4px; line-height: 1.45; color: var(--contact-red);
  }
  .contact__group { padding-right: 7px; border-right: 0.6px solid var(--contact-red); }
  .contact__group:last-child { border-right: none; padding-right: 0; }
  .contact__label { font-weight: 600; }
  .letter-body {
    position: absolute; top: 285px; left: 110px; width: 390px;
    font-size: 9.6px; line-height: 1.32; color: var(--ink);
    text-align: justify;
  }
  .letter-body p + p { margin-top: 12px; }
  .sign-off { position: absolute; top: 612px; left: 110px; }
  .sign-off__signature {
    width: 150px; height: 30px; border-radius: 14px;
    background: linear-gradient(90deg, rgba(44,63,166,.35), rgba(44,63,166,.12));
  }
  .sign-off__role { margin-top: 2px; font-size: 11px; color: var(--ink-soft); }
  .footer-band {
    position: absolute; left: 0; right: 0; bottom: 0; height: 110px;
    background: linear-gradient(90deg, var(--brand-orange) 0%, var(--amber) 55%, var(--rust) 100%);
  }
</style>
</head>
<body>
<main class="canvas">
  <article class="letterhead">
    <header class="letterhead__header">
      <div class="brand">
        <span class="brand__dot"></span>
        <span class="brand__name">Hartwell Legal</span>
      </div>
      <address class="contact">
        <div class="contact__group">
          <div><span class="contact__label">Phone</span> 212 555 01 84</div>
          <div><span class="contact__label">Cell</span> 917 555 02 63</div>
        </div>
        <div class="contact__group">
          <div><span class="contact__label">Email</span> office@hartwell-legal.example</div>
          <div><span class="contact__label">Web</span> www.hartwell-legal.example</div>
        </div>
        <div class="contact__group">
          <div>48 Mercer Lane</div>
          <div>Brookfield, NY 10482</div>
        </div>
      </address>
    </header>

    <section class="letter-body">
      <p>Letterhead samples are a great way of deciding what kind of letterhead you want to design for you and your company. The internet has a ton of great letterhead samples to browse through. Whether you want something simple, with just a couple lines of text of your business information, or something decorative and stunning, with photos and logos on the top and bottom of the page, it will be easy to find what you want, because there are samples online for basically any type of letterhead you could want.</p>
      <p>Any business could easily benefit from browsing through some letterhead samples, if only to get an idea for what kind of letterhead their company might want. Letterheads are just one of the tools that a business professional could use to help increase their customer base, and to really be memorable to everyone they write a letter to. Letterhead is quite an effective tool for marketing and advertising, but because it’s such a simple and well known idea, it is often unfairly overlooked. Make sure you don’t make that mistake, and make some letterhead samples of your own today.</p>
      <p>Whether you want to get new customers to remember you and become part of your clientele, or you just want to send out friendly reminders to your existing clients, customizing your own letterhead samples can really help you out. Try out some letterhead samples and you will not regret it, and I’m sure you will add a new tool to your business’ arsenal of networking, marketing, and advertising tools.</p>
    </section>

    <div class="sign-off">
      <div class="sign-off__signature" role="img" aria-label="Handwritten signature of Daniel Marlow"></div>
      <div class="sign-off__role">company director</div>
    </div>

    <div class="footer-band" role="img" aria-label="Decorative orange and rust wave ornament along the foot of the page"></div>
  </article>
</main>
</body>
</html>
```